Business Card Design

Cedar Gate Rentals
Cedar Gate Rentals is a high end home rental leasing company that provides exquisite properties in niche markets. We are a small family owned business that considers our clients not as renters, but as friends. Every property we buy must be brought up to our high standards before it is offered on the market. The properties that we lease are exceptional, "move in" ready homes. This allows for the client to take pride in their lease as if it was their own home. To put it another way; we do not lease a property that we would not live in ourselves.

Target Market(s)

Couples making $100K or more

Industry/Entity Type

Business

Requirements
Must have
• Some sort of logo
Nice to have
• good slogan
Should not have
• Pink

```html
<!DOCTYPE html>
<html lang="en">
<head>
<meta charset="utf-8">
<title>Cedar Gate Rentals – Business Card</title>
<link href="https://fonts.googleapis.com/css2?family=Montserrat:wght@600&family=Roboto:wght@400;500&display=swap" rel="stylesheet">
<style>
  :root {
    --backdrop: #2a2a2a;
    --paper: #ffffff;
    --ink: #4a4646;
    --charcoal: #3e3a3a;
    --slate: #5b5656;
    --slate-dark: #333030;
    --amber-light: #eab04f;
    --amber-deep: #d97f1e;
    --on-dark: #ffffff;
  }
  html, body {
    margin: 0;
    width: 1200px;
    height: 900px;
    overflow: hidden;
    background: var(--backdrop);
  }
  .business-card {
    position: absolute;
    left: 150px;
    top: 190px;
    width: 900px;
    height: 520px;
    background: var(--paper);
    border-radius: 6px;
    overflow: hidden;
    box-shadow: 0 18px 40px rgba(0,0,0,0.45);
  }
  .card-shapes {
    position: absolute;
    inset: 0;
  }
  .brand {
    position: absolute;
    left: 58px;
    top: 128px;
    display: flex;
    align-items: center;
    gap: 22px;
  }
  .brand-square {
    width: 46px;
    height: 46px;
    background: var(--amber-light);
  }
  .brand-name {
    margin: 0;
    font-family: "Montserrat", sans-serif;
    font-weight: 600;
    font-size: 68px;
    letter-spacing: -0.5px;
    color: var(--ink);
    line-height: 1;
  }
  .contact-list {
    position: absolute;
    left: 530px;
    top: 274px;
    margin: 0;
    padding: 0;
    list-style: none;
    font-family: "Roboto", sans-serif;
    font-size: 21px;
    color: var(--on-dark);
  }
  .contact-list li {
    display: flex;
    align-items: center;
    gap: 12px;
    height: 30px;
  }
  .contact-icon {
    width: 20px;
    height: 20px;
    fill: none;
    stroke: var(--on-dark);
    stroke-width: 1.8;
    flex: none;
  }
  .person {
    position: absolute;
    left: 48px;
    top: 330px;
    color: var(--on-dark);
    font-family: "Roboto", sans-serif;
  }
  .person-name {
    margin: 0;
    font-weight: 500;
    font-size: 42px;
    line-height: 1;
    padding-bottom: 10px;
    border-bottom: 2px solid var(--on-dark);
    width: 270px;
  }
  .person-title {
    margin: 6px 0 8px 14px;
    font-size: 16px;
    line-height: 1.2;
  }
  .phone-list {
    margin: 0 0 0 30px;
    padding: 0;
    list-style: none;
    font-size: 27px;
  }
  .phone-list li {
    display: flex;
    align-items: center;
    gap: 12px;
    height: 32px;
  }
  .phone-list .contact-icon {
    width: 22px;
    height: 22px;
  }
</style>
</head>
<body>
  <div class="business-card">
    <svg class="card-shapes" width="900" height="520" viewBox="0 0 900 520" aria-hidden="true">
      <defs>
        <linearGradient id="amber" x1="0" x2="1" y1="0" y2="0">
          <stop offset="0" stop-color="#eab04f"/>
          <stop offset="1" stop-color="#d97f1e"/>
        </linearGradient>
      </defs>
      <path d="M430,232 L900,220 L900,232 L436,244 Z" fill="url(#amber)"/>
      <path d="M0,300 L330,300 Q350,300 364,288 L396,262 Q408,252 424,252 L900,240 L900,520 L0,520 Z" fill="var(--charcoal)"/>
      <path d="M470,268 L900,260 L900,370 L528,374 Q510,374 502,360 Z" fill="url(#amber)"/>
      <path d="M0,318 L470,318 Q492,318 500,338 L516,390 Q520,410 500,410 L0,410 Z" fill="var(--slate)"/>
      <rect x="0" y="490" width="900" height="30" fill="var(--slate-dark)"/>
    </svg>

    <div class="brand">
      <span class="brand-square"></span>
      <h1 class="brand-name">Cedar Gate Rentals</h1>
    </div>

    <ul class="contact-list">
      <li>
        <svg class="contact-icon" viewBox="0 0 20 20"><circle cx="10" cy="10" r="8"/><ellipse cx="10" cy="10" rx="3.5" ry="8"/><line x1="2" y1="10" x2="18" y2="10"/></svg>
        www.cedargaterentals.com
      </li>
      <li>
        <svg class="contact-icon" viewBox="0 0 20 20"><rect x="2" y="4" width="16" height="12"/><polyline points="2,4 10,11 18,4"/></svg>
        hello@cedargaterentals.com
      </li>
      <li>
        <svg class="contact-icon" viewBox="0 0 20 20"><polyline points="2,10 10,3 18,10"/><rect x="5" y="9" width="10" height="9"/><rect x="8.5" y="13" width="3" height="5"/></svg>
        address area name city country
      </li>
    </ul>

    <div class="person">
      <h2 class="person-name">Your Name</h2>
      <p class="person-title">Your Title</p>
      <ul class="phone-list">
        <li>
          <svg class="contact-icon" viewBox="0 0 22 22"><path d="M3,9 Q11,3 19,9 L17,11 L14,9 L8,9 L5,11 Z"/><rect x="6" y="12" width="10" height="7"/></svg>
          555.214.6380
        </li>
        <li>
          <svg class="contact-icon" viewBox="0 0 22 22"><rect x="6" y="3" width="10" height="6"/><rect x="3" y="9" width="16" height="7"/><rect x="6" y="14" width="10" height="5"/></svg>
          555-873-1902
        </li>
      </ul>
    </div>
  </div>
</body>
</html>
```